Brambleway Farming

We need a logo design for a new company based in Kelowna, BC. We grow market garden vegetables for sale at market and in a CSA program. We try to only use hand tools for all aspects of cultivating, seeding, weeding, harvesting and distributing. For this reason we consider ourselves very low impact on the environment.

We would like blues and green in the design with an earthy, natural feel

Target Market(s)

Environmentally aware, health conscience

Industry/Entity Type

Farming

Requirements
Must have
• Foot prints with section for contact details all on the one side
Should not have
• Dark, black colours or anything that looks unnatural

```html
<!DOCTYPE html>
<html lang="en">
<head>
<meta charset="utf-8">
<title>Brambleway Farming – Business Card</title>
<link rel="stylesheet" href="https://fonts.googleapis.com/css2?family=Open+Sans:wght@400;600&display=swap">
<style>
  :root {
    --canvas-bg: #ecebe7;
    --leaf-green: #6cb547;
    --field-light: #78bd55;
    --field-dark: #4f9a35;
    --brand-blue: #1c74bb;
    --ink-grey: #6a6a6a;
    --rule-grey: #9a9a9a;
    --card-white: #ffffff;
  }
  * { margin: 0; padding: 0; box-sizing: border-box; }
  html, body { width: 1200px; height: 1000px; overflow: hidden; }
  body {
    background: var(--canvas-bg);
    font-family: "Open Sans", Arial, sans-serif;
    position: relative;
  }
  .card {
    position: absolute;
    left: 266px;
    width: 666px;
    height: 396px;
    overflow: hidden;
    box-shadow: 0 6px 18px rgba(0,0,0,0.18);
  }
  .card--front { top: 74px; }
  .card--back { top: 534px; background: var(--card-white); }

  .field-photo {
    position: absolute; inset: 0;
    background: linear-gradient(180deg, var(--field-dark) 0%, var(--field-light) 35%, var(--leaf-green) 70%, var(--field-dark) 100%);
  }
  .wordmark {
    position: absolute;
    font-weight: 400;
    line-height: 1;
  }
  .card--front .wordmark { left: 138px; top: 158px; color: var(--card-white); }
  .wordmark__name { display: block; font-size: 56px; letter-spacing: -1px; }
  .wordmark__sub { display: block; font-size: 30px; letter-spacing: 15px; margin-top: 14px; }
  .card--back .wordmark { left: 336px; top: 78px; color: var(--leaf-green); }
  .card--back .wordmark__name { font-size: 44px; }
  .card--back .wordmark__sub { font-size: 24px; letter-spacing: 12px; margin-top: 10px; }

  .holder { position: absolute; left: 34px; top: 192px; }
  .holder__flag {
    position: absolute; left: -34px; top: 4px;
    width: 9px; height: 36px; background: var(--leaf-green);
  }
  .holder__name { font-size: 22px; font-weight: 600; color: var(--leaf-green); line-height: 1.2; }
  .holder__role { font-size: 16px; color: var(--ink-grey); margin-top: 2px; }
  .divider {
    position: absolute; left: 32px; top: 252px;
    width: 602px; height: 2px; background: var(--rule-grey);
  }
  .contacts { position: absolute; left: 32px; top: 266px; list-style: none; }
  .contacts li {
    display: flex; align-items: center; gap: 8px;
    font-size: 16px; color: var(--ink-grey); height: 23.5px;
  }
  .contacts svg { width: 15px; height: 15px; fill: var(--leaf-green); flex: none; }
  .address {
    position: absolute; right: 32px; top: 288px;
    text-align: right; font-size: 16px; color: var(--ink-grey); line-height: 24px;
    font-style: normal;
  }
  .footer-bands { position: absolute; left: 0; bottom: 0; width: 666px; height: 36px; }
  .tagline {
    position: absolute; right: 18px; bottom: 6px;
    font-size: 18px; color: var(--card-white);
  }
</style>
</head>
<body>
  <section class="card card--front">
    <div class="field-photo" role="img" aria-label="Green-tinted photograph of crop rows stretching across a farm field"></div>
    <div class="wordmark">
      <span class="wordmark__name">Brambleway</span>
      <span class="wordmark__sub">FARMING</span>
    </div>
  </section>

  <section class="card card--back">
    <div class="wordmark">
      <span class="wordmark__name">Brambleway</span>
      <span class="wordmark__sub">FARMING</span>
    </div>

    <div class="holder">
      <span class="holder__flag"></span>
      <div class="holder__name">Marisol Hartley</div>
      <div class="holder__role">Managing Director</div>
    </div>
    <div class="divider"></div>

    <ul class="contacts">
      <li><svg viewBox="0 0 16 16"><path d="M1 5c0-2 3-3 7-3s7 1 7 3v1h-4V4.5H5V6H1z"/><path d="M3 8h10l1 6H2z"/></svg>+ 000 000 0000</li>
      <li><svg viewBox="0 0 16 16"><rect x="4" y="1" width="8" height="4"/><rect x="1" y="6" width="14" height="6" rx="1"/><rect x="4" y="10" width="8" height="5"/></svg>+ 000 000 0000</li>
      <li><svg viewBox="0 0 16 16"><path d="M1 3h14v2L8 9 1 5z"/><path d="M1 7l7 4 7-4v6H1z"/></svg>info@bramblewayfarming.com</li>
      <li><svg viewBox="0 0 16 16"><circle cx="8" cy="8" r="6.5" fill="none" stroke="var(--leaf-green)" stroke-width="2"/><path d="M2 8h12M8 2c3 3 3 9 0 12M8 2c-3 3-3 9 0 12" fill="none" stroke="var(--leaf-green)" stroke-width="1.3"/></svg>www.bramblewayfarming.com</li>
    </ul>

    <address class="address">2417 Orchard Vale Road,<br>Kelowna BC V1W 3K9</address>

    <svg class="footer-bands" viewBox="0 0 666 36" preserveAspectRatio="none" aria-hidden="true">
      <rect x="0" y="18" width="310" height="18" fill="var(--brand-blue)"/>
      <polygon points="290,36 326,0 666,0 666,36" fill="var(--leaf-green)"/>
    </svg>
    <div class="tagline">Freshly Picked Food from our Farm</div>
  </section>
</body>
</html>
```